Stationary Design For New Dynamic Company

Hi there we require stationary designed for our new company, we have used "Pixel Harbor" recently for our logo and were very impressed with all of the designers that contributed towards the final result.
What we require now is the following:
Letter head layout (A4)
Business Cards (5 people)
With Compliments slips
Envelopes
Email stationary
We would like to use our current logo design and I have included it for your use (JPEG is the one we have chosen and I have attached an EPS file for your use). Our company specializes in architectural cladding and our products are used by architects, builders and private clients, so we wish for the stationary to be suitable and attractive to our clientele.
I thank everyone in advance for your contributions.
Thank you to all that have provided your designs for this project, I apologize for not providing feedback as I have been away. I have looked at everyone's designs and they all look great and I will come back to those designers that I wish to have changes made sometime today.
Once again a big thank you to all involved.
Business

```html
<!DOCTYPE html>
<html lang="en">
<head>
<meta charset="utf-8">
<title>Veneria business cards</title>
<link rel="stylesheet" href="https://fonts.googleapis.com/css2?family=Jost:wght@400;600;700&display=swap">
<style>
  :root {
    --navy: #0b1150;
    --orange: #ef6a1f;
    --paper: #ffffff;
    --ink: #3a3a48;
    --muted: #6b6b78;
    --backdrop: #e9e9ec;
  }
  * { margin: 0; padding: 0; box-sizing: border-box; }
  html, body {
    width: 1200px; height: 800px; overflow: hidden;
    background: var(--backdrop);
    font-family: "Jost", "Century Gothic", sans-serif;
  }
  .stage {
    width: 1200px; height: 800px;
    display: flex; align-items: center; justify-content: center; gap: 60px;
  }
  .card {
    width: 520px; height: 316px;
    position: relative;
    box-shadow: 0 6px 20px rgba(0,0,0,0.18);
  }
  .card--front { background: var(--paper); color: var(--ink); }
  .card--back { background: var(--navy); }

  .brand {
    display: flex; align-items: center; gap: 10px;
    font-weight: 700; letter-spacing: 0.02em; line-height: 1;
  }
  .brand__mark { width: 20px; height: 20px; background: var(--orange); }
  .card--front .brand {
    position: absolute; left: 150px; top: 54px;
    font-size: 36px; color: var(--navy);
  }
  .card--back .brand {
    position: absolute; right: 40px; top: 48px;
    font-size: 28px; color: var(--paper);
  }

  .person {
    position: absolute; right: 40px; top: 112px; text-align: right;
  }
  .person__name { font-size: 21px; font-weight: 700; color: var(--navy); }
  .person__role { font-size: 15px; color: var(--muted); margin-top: -2px; }

  .contact {
    position: absolute; right: 40px; top: 182px; text-align: right;
    font-size: 15px; line-height: 1.3; color: var(--ink);
  }
  .address {
    position: absolute; right: 40px; bottom: 28px; text-align: right;
    font-size: 15px; line-height: 1.3; color: var(--ink);
  }
</style>
</head>
<body>
  <main class="stage">
    <section class="card card--front" aria-label="Business card front">
      <div class="brand"><span class="brand__mark"></span>VENERIA</div>
      <div class="person">
        <p class="person__name">Mara Ellison</p>
        <p class="person__role">director</p>
      </div>
      <div class="contact">
        <p>m 0491 570 263</p>
        <p>mara@veneria.com.au</p>
        <p>www.veneria.com.au</p>
      </div>
      <div class="address">
        <p>Suite 4, Linden Court Arcade</p>
        <p>17 Quarry Lane, Ashford</p>
      </div>
    </section>

    <section class="card card--back" aria-label="Business card back">
      <div class="brand"><span class="brand__mark"></span>VENERIA</div>
    </section>
  </main>
</body>
</html>
```